Bank Debit Card Design Project

A ten year old bank needs a new debit card design. The bank is young and brings a modern approach to banking that emphasizes customers. Located in Zigong China we need a card design that respectfully represents the bank, its simple process, and its innovation. This debit card design is to signify a new beginning, a fresh start.

We are looking for a design that embodies Zigong Culture and that does not look like someone else's card.

Customers are our central idea and we prefer eye catching bright or shiny Colors.

Attached are Briefs that will inform you on some of the local cultural icons.

The meaning behind your art is equally as important as your design. So please include explanations for the colors you use; for the shapes and any objects that you use; and an explanation for your layout/structure. We plan on sending this card across Asia and using it for a long time so we are looking for a card design that is not random but full of meaning.

Target Market(s)

Banking customers, professionals, and working class people

Industry/Entity Type

Bank

Font styles to use
Serif
Sans Serif
Decorative
Script

```html
<!DOCTYPE html>
<html lang="en">
<head>
<meta charset="utf-8">
<title>Saltwell Commercial Bank – Debit Card</title>
<link rel="stylesheet" href="https://fonts.googleapis.com/css2?family=IBM+Plex+Mono:wght@400;500&display=swap">
<style>
  :root {
    --canvas-bg: #ecebe8;
    --card-red-light: #ff3232;
    --card-red: #f2121c;
    --card-red-deep: #c40810;
    --mountain-dark: rgba(110, 0, 6, 0.75);
    --mountain-mid: rgba(170, 10, 16, 0.45);
    --card-ink: #ffffff;
    --card-shadow: rgba(60, 20, 20, 0.28);
  }
  * { box-sizing: border-box; margin: 0; padding: 0; }
  html, body {
    width: 1200px;
    height: 720px;
    overflow: hidden;
    background: var(--canvas-bg);
  }
  .canvas {
    position: relative;
    width: 1200px;
    height: 720px;
  }
  .debit-card {
    position: absolute;
    left: 170px;
    top: 89px;
    width: 860px;
    height: 542px;
    border-radius: 34px;
    overflow: hidden;
    background: linear-gradient(160deg, var(--card-red-light) 0%, var(--card-red) 45%, var(--card-red-deep) 100%);
    box-shadow: 0 18px 40px var(--card-shadow);
    color: var(--card-ink);
    font-family: "IBM Plex Mono", monospace;
  }
  .mountain-scene {
    position: absolute;
    right: 0;
    top: 0;
    width: 58%;
    height: 72%;
    background:
      radial-gradient(ellipse 60% 45% at 75% 55%, var(--mountain-dark) 0%, transparent 70%),
      linear-gradient(200deg, var(--mountain-mid) 0%, rgba(150, 5, 12, 0.25) 45%, transparent 80%);
    -webkit-mask-image: linear-gradient(to left, #000 55%, transparent 100%);
    mask-image: linear-gradient(to left, #000 55%, transparent 100%);
  }
  .bank-name {
    position: absolute;
    left: 52px;
    top: 66px;
    display: flex;
    align-items: center;
    gap: 12px;
    font-size: 24px;
    font-weight: 500;
    letter-spacing: 0.5px;
  }
  .bank-name .mark {
    width: 22px;
    height: 22px;
    border-radius: 50%;
    background: var(--card-ink);
  }
  .cardholder {
    position: absolute;
    left: 52px;
    top: 200px;
    font-size: 36px;
    letter-spacing: 1px;
  }
  .card-number {
    position: absolute;
    left: 52px;
    top: 318px;
    font-size: 38px;
    letter-spacing: 1px;
    line-height: 1.25;
  }
  .card-number .account-suffix { display: block; }
  .validity {
    position: absolute;
    left: 540px;
    top: 250px;
    font-size: 34px;
    line-height: 1.2;
    letter-spacing: 1px;
  }
  .validity .expiry { display: block; padding-left: 14px; }
</style>
</head>
<body>
  <main class="canvas">
    <section class="debit-card">
      <div class="mountain-scene" role="img" aria-label="Misty red-toned mountain range with forested slopes under clouds"></div>
      <div class="bank-name"><span class="mark"></span>SALTWELL COMMERCIAL BANK</div>
      <p class="cardholder">LENA MARCHETTI</p>
      <p class="card-number">4000 1234 5678 9010<span class="account-suffix">1224</span></p>
      <p class="validity">VALID THRU<span class="expiry">12/14</span></p>
    </section>
  </main>
</body>
</html>
```